Marnie's Fitness Business Cards

I would like my business cards to look expensive and sophisticated using my logo and the information below.

FRONT
Marnie’s Fitness logo

Tag line Become your happiest, healthiest and strongest self

Marnie Pulham Crisp
Personal Trainer

e. marnie@marniesfitness.example

t. 0781350462

w. www.marniesfitness.example

```html
<!DOCTYPE html>
<html lang="en">
<head>
<meta charset="utf-8">
<title>Marnie's Fitness Business Cards</title>
<link rel="stylesheet" href="https://fonts.googleapis.com/css2?family=Jost:ital,wght@0,300;0,400;0,500;1,300;1,500&display=swap">
<style>
  :root {
    --canvas: #e4e4e4;
    --teal: #6bbfc6;
    --teal-deep: #5aaeb5;
    --teal-light: #78c8ce;
    --paper: #ffffff;
    --ink: #4f4f4f;
    --ink-soft: #7a7a7a;
    --on-teal: #ffffff;
  }
  * { box-sizing: border-box; margin: 0; padding: 0; }
  html, body {
    width: 837px; height: 1200px; overflow: hidden;
    background: var(--canvas);
    font-family: "Jost", "Futura", sans-serif;
  }
  .sheet {
    width: 837px; height: 1200px;
    display: flex; flex-direction: column; align-items: center; justify-content: center;
    gap: 56px;
  }
  .card {
    position: relative;
    width: 740px; height: 423px;
    box-shadow: 0 6px 14px rgba(0,0,0,0.22);
    overflow: hidden;
  }

  /* Reverse side */
  .card--reverse {
    background: linear-gradient(160deg, var(--teal-light) 0%, var(--teal) 55%, var(--teal-deep) 100%);
    color: var(--on-teal);
  }
  .tagline {
    position: absolute; left: 0; right: 0; top: 182px;
    text-align: center; font-style: italic; font-weight: 300;
    font-size: 22px; line-height: 1.3; letter-spacing: 0.2px;
  }
  .tagline strong { font-weight: 500; }
  .reverse-web {
    position: absolute; left: 0; right: 0; bottom: 44px;
    text-align: center; font-size: 16px; font-weight: 300; letter-spacing: 0.5px;
  }
  .reverse-web strong { font-weight: 500; }

  /* Front side */
  .card--front { background: var(--paper); color: var(--ink); }
  .brand {
    position: absolute; right: 58px; top: 48px;
    display: flex; flex-direction: column; align-items: center; gap: 18px;
  }
  .brand-dot {
    width: 92px; height: 92px; border-radius: 50%;
    border: 6px solid var(--teal);
  }
  .brand-name {
    color: var(--teal); font-weight: 400; font-size: 20px;
    letter-spacing: 7px; text-transform: uppercase;
  }
  .person { position: absolute; left: 54px; top: 236px; }
  .person-name { color: var(--teal); font-weight: 500; font-size: 21px; }
  .person-role { color: var(--ink); font-weight: 400; font-size: 15px; margin-top: 1px; }
  .divider {
    position: absolute; left: 54px; right: 58px; top: 298px;
    height: 1.5px; background: var(--teal);
  }
  .contacts {
    position: absolute; left: 54px; top: 318px;
    list-style: none; font-size: 15px; line-height: 22px; color: var(--ink);
  }
  .contacts li { display: flex; align-items: center; gap: 8px; }
  .contacts svg { width: 12px; height: 12px; flex: none; }
</style>
</head>
<body>
<main class="sheet">
  <section class="card card--reverse" aria-label="Card reverse">
    <p class="tagline">Become your happiest,<br><strong>healthiest and strongest</strong> self</p>
    <p class="reverse-web">www.<strong>marniesfitness</strong>.example</p>
  </section>

  <section class="card card--front" aria-label="Card front">
    <div class="brand">
      <span class="brand-dot" aria-hidden="true"></span>
      <span class="brand-name">Marnie’s Fitness</span>
    </div>
    <div class="person">
      <p class="person-name">Marnie Pulham Crisp</p>
      <p class="person-role">Personal Trainer</p>
    </div>
    <div class="divider"></div>
    <ul class="contacts">
      <li>
        <svg viewBox="0 0 12 12" aria-hidden="true"><path d="M2.5 1 L4.5 1 L5.3 3.6 L4 4.6 Q5 7 7.4 8 L8.4 6.7 L11 7.5 L11 9.5 Q11 11 9.5 11 Q1 10.5 1 2.5 Q1 1 2.5 1 Z" fill="none" stroke="var(--teal)" stroke-width="1.1"/></svg>
        078 135 0462
      </li>
      <li>
        <svg viewBox="0 0 12 12" aria-hidden="true"><rect x="1" y="2.5" width="10" height="7" fill="none" stroke="var(--teal)" stroke-width="1.1"/><path d="M1 2.5 L6 6.5 L11 2.5" fill="none" stroke="var(--teal)" stroke-width="1.1"/></svg>
        marnie@marniesfitness.example
      </li>
      <li>
        <svg viewBox="0 0 12 12" aria-hidden="true"><circle cx="6" cy="6" r="5" fill="var(--teal)"/><path d="M1 6 H11 M6 1 Q9 6 6 11 Q3 6 6 1" fill="none" stroke="#fff" stroke-width="0.8"/></svg>
        www.marniesfitness.example
      </li>
    </ul>
  </section>
</main>
</body>
</html>
```